New Software Development Firm Needs Business Cards!

We just completed a successful logo design project on MakerHive and need to develop a business card design using that shiny new logo. We want a clean, modern design that communicates professionalism and tech savvy without being cliche'.

The company is "Bramble Logic, LLC", but our dba is "Bramble" The business card address should reflect the full company name in the address. The logo just uses "Bramble".

Photoshop or Illustrator source files will be required, along with exact font name(s) and source(s) used.

The design will need to work well with our letterhead as well. I'm also launching a project right now for letterhead and envelopes as well. Please submit to both projects! We're excited to see the designs. Thanks...

Target Market(s)

Small to medium business professionals

Industry/Entity Type

Business

Requirements
Must have
• Need place for:
- Company name and address (5 lines)
- Phone: (1 number)
- Fax: (1 number)
- Employee's name
- Employee's position
- Employee's email address
- Company web site URL
Nice to have
• Probably want a white card, but we're open to options.

```html
<!DOCTYPE html>
<html lang="en">
<head>
<meta charset="UTF-8">
<title>Bramble Logic, LLC — Business Card</title>
<link href="https://fonts.googleapis.com/css2?family=Open+Sans:wght@400;600;700&display=swap" rel="stylesheet">
<style>
  :root {
    --ink: #111111;
    --muted: #a6b0ad;
    --paper: #ffffff;
    --frame: #111111;
    --panel-grey: #e3e3e3;
    --panel-blush: #fde4e3;
  }
  * { margin: 0; padding: 0; box-sizing: border-box; }
  html, body {
    width: 927px; height: 1200px; overflow: hidden;
    background: var(--paper);
    font-family: "Open Sans", Arial, sans-serif;
  }
  .sheet { position: relative; width: 927px; height: 1200px; }
  .card {
    position: absolute; left: 42px; width: 791px; height: 511px;
    border: 3px solid var(--frame); background: var(--paper);
  }
  .card--front { top: 30px; }
  .card--back { top: 613px; }
  .text { position: absolute; line-height: 1; white-space: nowrap; }

  /* front */
  .front-brand { left: 0; right: 0; top: 118px; text-align: center; font-size: 64px; font-weight: 400; color: var(--ink); letter-spacing: 1px; }
  .front-brand-sub { left: 0; right: 0; top: 190px; text-align: center; font-size: 31px; color: var(--ink); letter-spacing: 4px; padding-left: 10px; }
  .front-numbers { left: 105px; top: 396px; font-size: 35px; color: var(--muted); letter-spacing: 4px; word-spacing: 14px; }
  .front-web { left: 105px; top: 449px; font-size: 33px; color: var(--ink); letter-spacing: 5px; }

  /* back */
  .back-panel { position: absolute; left: 20px; top: 30px; width: 451px; height: 450px; }
  .back-brand { right: 22px; top: 28px; font-size: 40px; color: var(--ink); }
  .back-name { right: 18px; top: 207px; font-size: 45px; font-weight: 700; color: var(--ink); letter-spacing: 4px; }
  .back-role { right: 20px; top: 254px; font-size: 35px; color: var(--muted); letter-spacing: 3px; }
  .back-email { right: 18px; top: 329px; font-size: 35px; color: var(--ink); letter-spacing: 3px; }
  .back-address { right: 22px; top: 440px; font-size: 24px; line-height: 32px; color: var(--muted); letter-spacing: 3px; text-align: right; }
</style>
</head>
<body>
<main class="sheet">
  <section class="card card--front" aria-label="Card front">
    <div class="text front-brand">Bramble</div>
    <div class="text front-brand-sub">Logic LLC</div>
    <div class="text front-numbers">P: 123456789 &nbsp;F: 123456789</div>
    <div class="text front-web">www.companywebsite.com</div>
  </section>

  <section class="card card--back" aria-label="Card back">
    <svg class="back-panel" viewBox="0 0 451 450" aria-hidden="true">
      <rect width="451" height="450" fill="var(--panel-blush)"/>
      <polygon points="0,0 451,450 0,450" fill="var(--panel-grey)"/>
    </svg>
    <div class="text back-brand">Bramble</div>
    <div class="text back-name">Forename Surname</div>
    <div class="text back-role">Employees Position</div>
    <div class="text back-email">E: name@bramble.com</div>
    <div class="text back-address">Company address, street, location<br>state, post/zip code</div>
  </section>
</main>
</body>
</html>
```